Academic acomlishments and book promotional business card

Must Present my accomplishments in a strong fashion while looking very professional. We will need to make last minute changes in book title in about one to two months so it can't close until then. Must place a great emphasis on peer review. Treat this as if it were my business. It is more important than my titles. Vary fond slightly to emphasize peer review.
Updates

Project Deadline Extended
Reason: I will need to make small changes in book title in a month or two so it can't close until then.

Target Market(s)

Scholars, employers, patrons, and professionals.

Industry/Entity Type

Business

Contact Information for Business Card

Basic content:

Miles T. Brenvorth
Peer review by: Halbrook University Press + Heron Books + F. K. Ravell Co. + Edgar Fennick & Sons

Evolutionary Scientist + Historian

Academic Consultant, Marlowe University Press

See Overleaf

quillmiles@mailbrook.com + Cell. (555) 218-7634

Reverse Side:

In the distant future I see open fields for far more important researches. Psychology will be based on a new foundation, that of the necessary squire Kent of each mental power by gradation. Light will be thrown on the origin of man and his history. --Henry Lowcastle [make dash one line]

Book: "Tribal Debt or Civic Debt: Adaptive Behaviour,..."

See Facebook for CV with Endorsements + Writing Sample.

Font styles to use
Serif

Requirements
Must have
• The font has to be big enough etc to be able to use the gold ink at printvela.com, who will print them. Pls see their website for specs.
Nice to have
• Have a capital of the last letter in the Greek alphabet as a decorative element. Though this is not necessary.
Should not have
• Not Ornate or very curvalinear font.

```html
<!DOCTYPE html>
<html lang="en">
<head>
<meta charset="utf-8">
<title>Tribal Debt or Civic Debt — Business Card Reverse</title>
<link rel="stylesheet" href="https://fonts.googleapis.com/css2?family=Cinzel:wght@500;600;700&display=swap">
<style>
  :root {
    --teal: #0b8b7b;
    --paper: #ffffff;
    --ink: #2a2a2a;
    --light: #ffffff;
  }
  html, body {
    margin: 0;
    padding: 0;
    width: 1200px;
    height: 686px;
    overflow: hidden;
    background: var(--paper);
  }
  .card {
    position: relative;
    width: 1200px;
    height: 686px;
    overflow: hidden;
    font-family: "Cinzel", "Trajan Pro", serif;
  }
  .top-band {
    position: absolute;
    left: 0; top: 0;
    width: 100%;
    height: 49px;
    background: var(--teal);
  }
  .quote-panel {
    position: absolute;
    left: 0; top: 49px;
    width: 100%;
    height: 294px;
    background: var(--paper);
    color: var(--ink);
    text-align: center;
  }
  .quote {
    margin: 0;
    position: absolute;
    left: 0; right: 0;
    top: 44px;
    font-weight: 700;
    font-size: 20px;
    line-height: 38.5px;
    letter-spacing: 0.6px;
  }
  .quote-line { display: block; }
  .quote-author {
    position: absolute;
    left: 0; right: 0;
    top: 220px;
    margin: 0;
    font-weight: 700;
    font-size: 20px;
    letter-spacing: 0.6px;
  }
  .book-panel {
    position: absolute;
    left: 0; top: 343px;
    width: 100%;
    height: 343px;
    background: var(--teal);
    color: var(--light);
    text-align: center;
  }
  .book-label {
    position: absolute;
    left: 0; right: 0;
    top: 42px;
    margin: 0;
    font-weight: 600;
    font-size: 38px;
    letter-spacing: 0.5px;
  }
  .book-title {
    position: absolute;
    left: 0; right: 0;
    top: 104px;
    margin: 0;
    font-weight: 600;
    font-size: 58px;
    line-height: 1;
    white-space: nowrap;
  }
  .book-title .title-part { letter-spacing: 2px; }
  .book-title .title-part.spaced { letter-spacing: 9px; }
  .book-title .conjunction {
    font-size: 30px;
    letter-spacing: 1px;
    margin: 0 6px 0 10px;
    vertical-align: 8px;
  }
  .peer-review {
    position: absolute;
    left: 0; right: 0;
    top: 208px;
    margin: 0;
    font-weight: 700;
    font-size: 32px;
    line-height: 46px;
    letter-spacing: 0.6px;
  }
  .peer-review span { display: block; }
</style>
</head>
<body>
  <main class="card">
    <div class="top-band"></div>

    <section class="quote-panel">
      <blockquote class="quote">
        <span class="quote-line">In the distant future I see open fields for far more important researches.</span>
        <span class="quote-line">Psychology will be based on a new foundation,</span>
        <span class="quote-line">that of the necessary acquirement of each mental power by gradation.</span>
        <span class="quote-line">Light will be thrown on the origin of man and his history.</span>
      </blockquote>
      <p class="quote-author">Henry Lowcastle</p>
    </section>

    <section class="book-panel">
      <p class="book-label">MILES’ BOOK</p>
      <h1 class="book-title">
        <span class="title-part">TRIBAL DEBT</span><span class="conjunction">OR</span><span class="title-part spaced">CIVIC DEBT</span>
      </h1>
      <p class="peer-review">
        <span>CV and writing sample with peer review</span>
        <span>available upon request</span>
      </p>
    </section>
  </main>
</body>
</html>
```